Letterhead Design Project

We have just had a letterhead desinged on word which is pretty basic and boring. We are looking for a professional and modern letterhead to suit our business for letters and quotes. We are an irrigation business that looks at providing a garden enhancement package. We do instore sales, internet sales and design and installation. We would like the colours to be similar to what is on our website. www.dunsfordwatering.com.au
Industry/Entity Type
Internet
Requirements
Must have
- We would like to include:
find us on plain square and plain square,
member of sprinquest stores,
Catchphrase: "Your Complete Garden Watering Partner"
Approved Watering Stockist Logo
phone, fax, email & website

```html
<!DOCTYPE html>
<html lang="en">
<head>
<meta charset="utf-8">
<title>Dunsford Watering Letterhead</title>
<link href="https://fonts.googleapis.com/css2?family=Open+Sans:wght@400;600;700&display=swap" rel="stylesheet">
<style>
  :root {
    --page: #ffffff;
    --backdrop: #e9eaec;
    --ink: #333333;
    --ink-soft: #555555;
    --brand-blue: #1f6fb2;
    --brand-light: #9fcdf0;
    --brand-green: #3a8a2e;
    --rule: #bdbdbd;
    --watermark: #f1f5f8;
  }
  * { margin: 0; padding: 0; box-sizing: border-box; }
  html, body { width: 1058px; height: 1200px; overflow: hidden; background: var(--backdrop); }
  body { font-family: "Open Sans", Arial, sans-serif; color: var(--ink); }
  .letterhead { position: relative; width: 1058px; height: 1200px; background: var(--page); overflow: hidden; }

  .brand { position: absolute; top: 60px; left: 0; width: 100%; text-align: center; }
  .brand-name { display: inline-flex; align-items: center; gap: 10px; padding: 8px 18px; font-size: 28px; font-weight: 600; color: var(--brand-blue); background: #eaf3fb; }
  .brand-mark { width: 22px; height: 22px; background: var(--brand-light); }
  .brand-tagline { margin-top: 6px; font-size: 17px; font-weight: 600; color: #222; letter-spacing: 0.4px; }

  .margin-rule { position: absolute; left: 152px; top: 300px; width: 1px; height: 850px; background: var(--rule); }
  .social { position: absolute; left: 112px; top: 720px; display: flex; flex-direction: column; align-items: center; gap: 6px; }
  .social-square { width: 22px; height: 22px; background: var(--brand-blue); }
  .social-square.light { background: var(--brand-light); }
  .social-label { writing-mode: vertical-rl; transform: rotate(180deg); font-size: 13px; color: var(--ink-soft); margin-top: 8px; }
  .side-web { position: absolute; left: 112px; top: 890px; height: 230px; writing-mode: vertical-rl; transform: rotate(180deg); font-size: 14px; color: var(--ink-soft); }
  .side-web b { color: var(--brand-blue); font-weight: 600; }

  .watermark { position: absolute; left: 560px; top: 560px; width: 220px; height: 220px; border-radius: 50%; background: var(--watermark); }

  .recipient { position: absolute; left: 190px; top: 250px; font-size: 17px; line-height: 1.4; color: var(--ink-soft); font-style: normal; }
  .recipient strong { color: #111; font-weight: 700; }

  .letter-body { position: absolute; left: 228px; top: 405px; width: 660px; font-size: 16px; line-height: 1.6; color: var(--ink-soft); }
  .letter-body p { text-align: justify; margin-bottom: 28px; }
  .letter-body p.closing { text-align: left; }

  .signature { position: absolute; left: 290px; top: 920px; font-size: 16px; line-height: 1.45; color: var(--ink-soft); }
  .signature .sign-name { font-size: 17px; color: #111; }

  .partners { position: absolute; right: 110px; top: 1000px; display: flex; align-items: center; gap: 22px; }
  .member { font-size: 13px; font-weight: 700; color: var(--brand-green); line-height: 1.2; }
  .member strong { display: block; font-size: 19px; }
  .badge { width: 74px; height: 74px; border-radius: 50%; background: var(--brand-blue); border: 4px solid var(--brand-light); }
  .footer-rule { position: absolute; left: 690px; top: 1090px; width: 270px; height: 1px; background: var(--rule); }

  .footer { position: absolute; left: 220px; top: 1125px; font-size: 14px; color: var(--ink-soft); display: flex; gap: 14px; align-items: center; }
  .footer svg { width: 13px; height: 13px; vertical-align: -2px; margin-right: 4px; }
</style>
</head>
<body>
<div class="letterhead">
  <header class="brand">
    <div class="brand-name"><span class="brand-mark"></span>Dunsford Watering Supplies</div>
    <div class="brand-tagline">Your Complete Garden Watering Partner</div>
  </header>

  <div class="margin-rule"></div>
  <div class="social">
    <span class="social-square"></span>
    <span class="social-square light"></span>
    <span class="social-label">find us on</span>
  </div>
  <div class="side-web">www.<b>dunsfordwatering</b>.com.au</div>

  <div class="watermark"></div>

  <address class="recipient">
    <strong>Mr. Daniel Hart</strong><br>
    Managing Director<br>
    USA Investor<br>
    42 W Harbor Street<br>
    USA
  </address>

  <main class="letter-body">
    <p>Lorem Ipsum is simply dummy text for printing and typesetting industry. Lorem Ipsum has been the industry's standard dummy text since the 1500s, when an unknown printer galley of type and scrambled it to make a type specimen book. It has survived not only manual but also the leap into electronic typesetting, remaining essentially unchanged. It was popularised in the 1960s with the release of Transfera sheets containing Lorem Ipsum pass and more recently with desktop publishing software like Folio PageStudio including version 6.9 of Lorem Ipsum.</p>
    <p>Contrary to popular belief, Lorem Ipsum is not simply random text. It has roots in a piece of classical Latin literature from 45 BC, making it over 2000 years old. Peter Lindqvist, a professor at Ashbury College in Vermont, looked up one of the most obscure words of classical literature and discovered the undoubtable source. Lorem Ipsum comes from section 1.10.32 and 1.10.33 of "de Rebus Hortorum et Aquarum" (The Extremes of Good and Evil by Varro Minor), written in 45 BC. This book is a treatise on the theory of ethics very popular during the Renaissance.</p>
    <p class="closing">Thank you for being one of our valued customers.</p>
  </main>

  <div class="signature">
    <div class="sign-name">Name Here</div>
    CEO<br>
    Dunsford Watering
  </div>

  <div class="partners">
    <div class="member">A member of<strong>SPRINQUEST</strong></div>
    <div class="badge" role="img" aria-label="Approved Watering Stockist badge"></div>
  </div>
  <div class="footer-rule"></div>

  <footer class="footer">
    <span>218 Kingsway Rd Dunsford.</span>
    <span><svg viewBox="0 0 16 16"><path fill="#1f6fb2" d="M4 1l3 3-2 2c1 2 3 4 5 5l2-2 3 3-2 3C7 15 1 9 1 3z"/></svg>03 9000 4127</span>
    <span><svg viewBox="0 0 16 12"><rect x="0.5" y="0.5" width="15" height="11" fill="none" stroke="#1f6fb2"/><path d="M1 1l7 6 7-6" fill="none" stroke="#1f6fb2"/></svg>sales@dunsfordwatering.com.au</span>
  </footer>
</div>
</body>
</html>
```